Stationery Design Project for import company - Kelvo Trading

We are a import company that sells branded products to large retailers in New Zealand.
We need a simple, professional looking Logo, Business Cards, Email Signature and Letterhead.
Design needs to have some colour in it but nothing too bright or youthful.
The brand is business to business.
The companies name is Kelvo Trading.
I have uploaded some examples of business cards that I like
Also need a powerpoint template
The range of products is diverse so the deign needs to be generic. Please note that the business does not sell to consumers only other businesses
Target Market(s)
Buyers at Retail Companies Head Offices (business to business)
Industry/Entity Type
Business
Look and feel
Each slider illustrates characteristics of the customer's brand and the style your logo design should communicate.

```html
<!DOCTYPE html>
<html lang="en">
<head>
<meta charset="utf-8">
<title>Kelvo Trading — Business Card</title>
<link rel="stylesheet" href="https://fonts.googleapis.com/css2?family=Marcellus+SC&family=Didact+Gothic&display=swap">
<style>
  :root {
    --backdrop: #1b1d21;
    --card-white: #ffffff;
    --card-fog: #e9edf2;
    --navy: #0b3763;
    --navy-deep: #082a4d;
    --ocean: #1f86b8;
    --ocean-deep: #0c5a86;
    --ink: #4a4f56;
    --faint-globe: #dbe4ee;
  }
  * { box-sizing: border-box; margin: 0; padding: 0; }
  html, body { width: 1200px; height: 871px; overflow: hidden; }
  body {
    background: var(--backdrop);
    font-family: "Didact Gothic", "Helvetica Neue", Arial, sans-serif;
    position: relative;
  }
  .card {
    position: absolute;
    width: 665px;
    height: 380px;
    overflow: hidden;
  }
  /* back side */
  .card--back {
    left: 60px; top: 40px;
    background: linear-gradient(135deg, var(--ocean) 0%, var(--ocean-deep) 100%);
  }
  .back-mark {
    position: absolute;
    left: 50%; top: 50%;
    transform: translate(-50%, -50%);
    display: flex; align-items: center; gap: 22px;
    white-space: nowrap;
  }
  .back-mark .dot {
    flex: 0 0 70px;
    width: 70px; height: 70px; border-radius: 50%;
    background: rgba(255,255,255,0.35);
  }
  .back-mark .word {
    font-family: "Marcellus SC", Georgia, serif;
    font-size: 40px; letter-spacing: 2px;
    color: rgba(255,255,255,0.8);
  }
  /* front side */
  .card--front {
    left: 475px; top: 451px;
    background: linear-gradient(160deg, var(--card-white) 55%, var(--card-fog) 100%);
  }
  .brand {
    position: absolute; left: 34px; top: 30px;
    display: flex; align-items: center;
    white-space: nowrap;
  }
  .brand .dot {
    flex: 0 0 40px;
    width: 40px; height: 40px; border-radius: 50%;
    background: var(--ocean);
  }
  .brand .divider {
    flex: 0 0 1px;
    width: 1px; height: 40px; background: #b9c3cd; margin: 0 12px 0 16px;
  }
  .brand .word {
    font-family: "Marcellus SC", Georgia, serif;
    font-size: 26px; color: var(--navy); letter-spacing: 1px;
  }
  .faint-globe {
    position: absolute; right: 30px; top: 105px;
    width: 230px; height: 230px; border-radius: 50%;
    background: var(--faint-globe); opacity: 0.7;
  }
  .contact {
    position: absolute; left: 34px; top: 130px;
    font-size: 14px; line-height: 17px; color: var(--ink);
    font-style: normal;
    white-space: nowrap;
  }
  .contact b { font-weight: normal; color: var(--navy); }
  .contact .web strong { color: var(--ink); font-weight: bold; }
  .person {
    position: absolute; left: 365px; top: 200px;
    white-space: nowrap;
  }
  .person .name { font-size: 25px; color: var(--navy); line-height: 26px; }
  .person .role { font-size: 18px; color: var(--ink); }
  .band-navy {
    position: absolute; left: 0; bottom: 0;
    width: 530px; height: 28px; background: var(--navy-deep);
  }
  .band-ocean {
    position: absolute; left: 542px; bottom: 0;
    width: 123px; height: 28px; background: var(--ocean);
  }
</style>
</head>
<body>
  <section class="card card--back" aria-label="Card back">
    <div class="back-mark">
      <span class="dot"></span>
      <span class="word">Kelvo Trading</span>
    </div>
  </section>

  <section class="card card--front" aria-label="Card front">
    <div class="faint-globe"></div>
    <div class="brand">
      <span class="dot"></span>
      <span class="divider"></span>
      <span class="word">Kelvo Trading</span>
    </div>
    <address class="contact">
      48 Harbour Lane, Auckland<br>
      1010, New Zealand<br>
      <b>P</b> : 09 555 0142<br>
      <b>C</b>: 000 000 0000<br>
      <b>F</b> : 000 000 0000<br>
      <b>E</b> : tobias@kelvotrading.com<br>
      <span class="web">www.<strong>KelvoTrading</strong>.com</span>
    </address>
    <div class="person">
      <p class="name">Tobias Wrenfield</p>
      <p class="role">President</p>
    </div>
    <div class="band-navy"></div>
    <div class="band-ocean"></div>
  </section>
</body>
</html>
```